依頼詳細
載内容詳細に関しては、別添のExcel資料を参照してください。

・ターゲット
BtoB
木工架装を出来る業者を探している車のリース販売会社の担当様

・カラーイメージ
木目デザインと企業カラーである紺色を使用してデザインお願いします
▼木目参考
https://www.haruki-mokuzai.jp/
▼紺参考
https://www.tmr-w.jp/

・デザイン、ムード
木を扱う仕事なので、木目を上手く使ってデザインしてほしい
▼参考

・JQについて
JQのパターン制作は不要です。
1枚目の画像でデザインお願いします

配置やデザイン等はアレンジしていただいて構いません。
また、縦に制限はありません。

レスポンシブデザインのサイトで、bootstrap4を利用しコーディングする予定になります。

デザイン幅は2000px、コンテンツの幅はbootstrap4デフォルトのの1110pxを基準としてください。
ただし、最近のデザインの流行を取りいれて、フルワイドや、1200~15000px程度の幅のコンテンツをバランスよくレイアウトしてください。
コンテンツ配置は基本12分割になります。がデザインによっては、多少逸脱してもかまいません。
bootstrap4、12分割グリッドの基準のPSDも資料として添付しております。
ご参考になさってください。

本分のフォントはゴシック系は游ゴシック、メイリオ、明朝系は遊明朝でお願いします。
飾り文字はフリーフォントか、googleフォントを利用してください。

メイン画像部分・グローバルメニューは、ワイド適用でお願いします。

不明点、質問などありましたらメッセージ等でご連絡ください。
サイトURL
ページ数
1ページ
希望イメージ
シンプル 複雑
単色 カラフル
暗い 明るい
日常 高級
遊び心 厳粛
未来的 伝統的
女性的 男性的
希望する色
青系、水色系
納品ファイル
• 高解像度JPG (.jpg)
• フォトショップ形式 (.psd)
補足説明
・資料上はサイト名(社名)や住所などは伏字にしております。
ご提案時点ではそのまま作成をお願いします。

・使用画像は当選後こちらで用意します。
ご提案時点では前項同様に、カンプデータ等をご使用のうえ、当選後に本内容へ差し替え修正をお願いします。
また、雰囲気が合っていれば、指定外の画像を追加掲載いただいてOKです。

・当選前提となった方は正式な社名及び連絡先をお伝えしますので修正対応をお願いします。
また希望の際は、当選後、中ページの制作及びコーディングも別途ご依頼可能です。

```html
<!DOCTYPE html>
<html lang="ja">
<head>
<meta charset="utf-8">
<title>○○○○ | 車内の木工架装施工専門業者</title>
<link href="https://fonts.googleapis.com/css2?family=Noto+Sans+JP:wght@400;500;700&family=Noto+Serif+JP:wght@500;700&family=Oswald:wght@400;500&display=swap" rel="stylesheet">
<style>
:root{
  --navy:#1d3170;
  --navy-dark:#14244f;
  --wood-light:#e3c9a3;
  --wood-mid:#c99e6c;
  --wood-dark:#8a5a31;
  --beige:#efe6da;
  --accent:#a5463a;
  --text:#333;
  --gray:#8d8d8d;
  --white:#fff;
}
*{margin:0;padding:0;box-sizing:border-box}
html,body{width:1200px;height:3504px;overflow:hidden}
body{position:relative;background:var(--white);font-family:"Noto Sans JP",sans-serif;color:var(--text)}
.abs{position:absolute}
.photo{position:absolute}

/* header + hero */
.wood-bg{position:absolute;left:0;top:0;width:1200px;height:680px;
  background:linear-gradient(90deg,var(--wood-light),#d9b98e 50%,var(--wood-light))}
.brand{left:40px;top:20px}
.brand small{display:block;font-size:11px;color:#4a3a2a;letter-spacing:.05em}
.brand strong{display:block;font-size:34px;font-weight:700;color:var(--navy-dark);letter-spacing:.08em;line-height:1.2}
.badge{left:240px;top:26px;width:46px;height:46px;background:var(--navy)}
.nav{left:420px;top:40px;display:flex;gap:42px;font-size:13px;color:#3a2b1d;font-weight:500}
.nav .on{border-bottom:2px solid var(--navy);padding-bottom:4px}
.tel{left:880px;top:38px;font-size:15px;font-weight:700;color:var(--navy-dark);display:flex;align-items:center;gap:6px}
.head-btn{left:1010px;top:28px;width:150px;height:42px;background:var(--navy);color:#fff;font-size:13px;display:flex;align-items:center;justify-content:center;gap:6px}
.hero-photo{left:240px;top:100px;width:960px;height:500px;background:linear-gradient(135deg,#5d4a3a,#c8884a 40%,#e2a867 60%,#7b6656)}
.hero-copy{left:140px;top:250px;color:#fff}
.hero-copy h1{font-family:"Noto Serif JP",serif;font-size:42px;font-weight:700;letter-spacing:.06em}
.hero-copy p{font-family:"Noto Serif JP",serif;font-size:24px;line-height:1.7;margin-top:40px;letter-spacing:.05em}
.hero-en{left:140px;top:560px;font-family:"Oswald",sans-serif;font-size:86px;color:#8a8580;letter-spacing:.01em;line-height:1.3}

/* about */
.about-photo{left:0;top:820px;width:520px;height:520px;background:linear-gradient(160deg,#3d3d3f,#b36a2f 45%,#d68a44 70%,#6b5040)}
.about-en{left:20px;top:1250px;font-size:58px;line-height:1.15;color:var(--wood-mid);font-weight:500}
.sec-line{width:56px;height:4px;background:var(--navy)}
.about-text{left:592px;top:1000px;width:540px}
.about-text h2{font-size:34px;font-weight:700;color:var(--navy-dark);line-height:1.45;margin-top:18px}
.about-text h3{font-size:19px;font-weight:500;color:var(--accent);margin-top:36px;line-height:1.6}
.about-text p{font-size:13px;line-height:2;margin-top:26px}

/* business */
.biz-panel{left:0;top:1670px;width:680px;height:490px;background:var(--beige)}
.biz-photo{left:580px;top:1610px;width:620px;height:470px;background:linear-gradient(150deg,#2e2e30,#9c5424 40%,#c67d3d 65%,#5b4a40)}
.biz-en{left:600px;top:1955px;font-size:64px;color:rgba(255,255,255,.85);font-weight:500}
.biz-text{left:144px;top:1790px;width:380px}
.biz-text h2{font-size:28px;color:var(--navy-dark);font-weight:700;margin-top:14px}
.biz-text p{font-size:13px;line-height:2;margin-top:24px}
.btn{position:absolute;background:var(--navy);color:#fff;font-size:13px;display:flex;align-items:center;justify-content:center}

/* works */
.works-head{left:0;top:2330px;width:1200px;text-align:center}
.works-head .sec-line{margin:0 auto}
.works-head h2{font-size:28px;color:var(--navy-dark);font-weight:700;margin-top:14px}
.w1{left:0;top:2440px;width:392px;height:220px;background:linear-gradient(150deg,#4a4240,#c07a3e 50%,#e0a465)}
.w2{left:402px;top:2440px;width:340px;height:220px;background:linear-gradient(160deg,#d9d6d0,#b9773b 55%,#efe0c8)}
.w3{left:752px;top:2440px;width:448px;height:220px;background:linear-gradient(140deg,#3e3a38,#a86530 50%,#d79858)}

/* contact */
.contact-photo{left:0;top:2950px;width:560px;height:470px;background:linear-gradient(150deg,#cbb79f,#8e6a48 50%,#e2d3c0)}
.contact-en{left:170px;top:3080px;font-size:70px;color:#9c5b3c;font-weight:500}
.contact-panel{left:560px;top:2950px;width:640px;height:470px;background:var(--beige)}
.contact-box{left:560px;top:3110px;width:640px;text-align:center}
.contact-box .sec-line{margin:0 auto}
.contact-box h2{font-size:28px;color:var(--navy-dark);font-weight:700;margin-top:14px}
.contact-box p{font-size:17px;margin-top:18px}
.tel-btn{left:700px;top:3250px;width:360px;height:52px;border:2px solid var(--navy);color:var(--navy-dark);font-size:16px;font-weight:700;display:flex;align-items:center;justify-content:center;gap:8px;background:#fff}
.mail-btn{left:700px;top:3326px;width:360px;height:52px;font-size:15px;gap:8px}

/* footer */
.footer{left:0;top:3420px;width:1200px;height:84px;background:#f4eee6}
.f-brand{left:40px;top:3432px;font-size:10px;line-height:1.5;color:#444}
.f-brand strong{font-size:22px;color:var(--navy-dark);letter-spacing:.08em;display:block}
.f-nav{left:620px;top:3454px;display:flex;gap:36px;font-size:12px;color:#444}
.f-copy{left:1110px;top:3456px;font-size:10px;color:var(--gray)}
</style>
</head>
<body>

<section class="top">
  <div class="wood-bg" role="img" aria-label="明るい木目の板の背景"></div>
  <div class="abs brand"><small>車内の木工架装施工専門業者</small><strong>○○○○</strong></div>
  <div class="abs badge"></div>
  <nav class="abs nav"><span class="on">HOME</span><span>業務内容</span><span>施工事例</span><span>会社案内</span></nav>
  <div class="abs tel">
    <svg width="14" height="14" viewBox="0 0 24 24"><path fill="#1d3170" d="M6.6 10.8a15 15 0 006.6 6.6l2.2-2.2c.3-.3.7-.4 1-.2 1.1.4 2.3.6 3.6.6.6 0 1 .4 1 1V20c0 .6-.4 1-1 1A17 17 0 013 4c0-.6.4-1 1-1h3.5c.6 0 1 .4 1 1 0 1.3.2 2.5.6 3.6.1.3 0 .7-.2 1z"/></svg>
    0000-11-2222</div>
  <div class="abs head-btn">
    <svg width="16" height="12" viewBox="0 0 16 12"><rect x=".5" y=".5" width="15" height="11" fill="none" stroke="#fff"/><path d="M.5.5L8 7l7.5-6.5" fill="none" stroke="#fff"/></svg>
    お問い合わせ</div>
  <div class="photo hero-photo" role="img" aria-label="木工架装を施した車の荷室の写真"></div>
  <div class="abs hero-copy">
    <h1>木工架装施工専門業者　○○○○</h1>
    <p>きめ細かいこだわりと<br>お客様のご要望を叶える確かな技術</p>
  </div>
  <div class="abs hero-en">Mizunoya Woodworking</div>
</section>

<section>
  <div class="photo about-photo" role="img" aria-label="木製の床を施工した車内の写真"></div>
  <div class="abs about-en">Woodworking<br>in the car</div>
  <div class="abs about-text">
    <div class="sec-line"></div>
    <h2>車内の木工架装工事なら<br>○○○○にご相談ください！</h2>
    <h3>"安心・確実"お客様のご要望に、<br>確かな技術でお応えいたします。</h3>
    <p>当社は創業以来、車内の木工架装を専門に手がけてまいりました。床張りや棚の設置など、用途に合わせた施工をご提案いたします。素材選びから仕上げまで、一台一台丁寧に対応いたします。まずはお気軽にご相談ください。</p>
  </div>
</section>

<section>
  <div class="abs biz-panel"></div>
  <div class="photo biz-photo" role="img" aria-label="木目の床板を敷いた車内の写真"></div>
  <div class="abs biz-en">Business</div>
  <div class="abs biz-text">
    <div class="sec-line"></div>
    <h2>業務内容</h2>
    <p>車内の床張り、棚や収納の製作など、木工架装全般を承っております。車種や用途に合わせて最適な施工をご提案いたします。</p>
  </div>
  <div class="btn" style="left:144px;top:2060px;width:240px;height:44px">業務内容</div>
</section>

<section>
  <div class="abs works-head"><div class="sec-line"></div><h2>施工事例</h2></div>
  <div class="photo w1" role="img" aria-label="施工事例：荷室の木製床"></div>
  <div class="photo w2" role="img" aria-label="施工事例：木製の荷台架装"></div>
  <div class="photo w3" role="img" aria-label="施工事例：車内の床張り"></div>
  <div class="btn" style="left:480px;top:2770px;width:240px;height:46px">すべて見る</div>
</section>

<section>
  <div class="photo contact-photo" role="img" aria-label="木工作業の様子の写真"></div>
  <div class="abs contact-en">Contact</div>
  <div class="abs contact-panel"></div>
  <div class="abs contact-box">
    <div class="sec-line"></div>
    <h2>お問い合わせ</h2>
    <p>ご依頼、ご質問等お気軽にお問い合わせください。</p>
  </div>
  <div class="abs tel-btn">
    <svg width="16" height="16" viewBox="0 0 24 24"><path fill="#1d3170" d="M6.6 10.8a15 15 0 006.6 6.6l2.2-2.2c.3-.3.7-.4 1-.2 1.1.4 2.3.6 3.6.6.6 0 1 .4 1 1V20c0 .6-.4 1-1 1A17 17 0 013 4c0-.6.4-1 1-1h3.5c.6 0 1 .4 1 1 0 1.3.2 2.5.6 3.6.1.3 0 .7-.2 1z"/></svg>
    0000-11-2222</div>
  <div class="btn mail-btn">
    <svg width="16" height="12" viewBox="0 0 16 12"><rect x=".5" y=".5" width="15" height="11" fill="none" stroke="#fff"/><path d="M.5.5L8 7l7.5-6.5" fill="none" stroke="#fff"/></svg>
    お問い合わせ</div>
</section>

<footer>
  <div class="abs footer"></div>
  <div class="abs f-brand">車内の木工架装施工専門業者<strong>○○○○</strong>〒000-0000 ○○県○○市○○町0-0-0　TEL 0000-11-2222</div>
  <nav class="abs f-nav"><span>HOME</span><span>業務内容</span><span>施工事例</span><span>会社案内</span><span>お問い合わせ</span></nav>
  <div class="abs f-copy">© ○○○○</div>
</footer>

</body>
</html>
```